Need Business Card for eLearning Company

Need a business card designed for our company, CareerPathlane.

CareerPathlane has developed a complete 12 lesson eLearning course to teach you the skills you need to present yourself in a job interview. The course uses advanced learning techniques in the multimedia videos, plus contains quizzes and additional exercises to insure you get the course and can walk into any interview with confidence and ease, and get the job.

www.careerpathlane-demo.com

Attached is our logo

Industry/Entity Type

Business

```html
<!DOCTYPE html>
<html lang="en">
<head>
<meta charset="utf-8">
<title>CareerPathlane Business Card</title>
<link rel="stylesheet" href="https://fonts.googleapis.com/css2?family=Roboto+Condensed:wght@400;700&display=swap">
<style>
  :root {
    --stage: #2b2b2b;
    --card-white: #ffffff;
    --card-grey: #e9e9e9;
    --brand-purple: #8e1f7f;
    --brand-purple-light: #b03a9e;
    --ink-dark: #3a3a3a;
    --on-purple: #ffffff;
  }
  * { margin: 0; padding: 0; box-sizing: border-box; }
  html, body {
    width: 1200px; height: 901px; overflow: hidden;
    background: var(--stage);
    font-family: "Roboto Condensed", Arial, sans-serif;
  }
  .stage { position: relative; width: 1200px; height: 901px; }

  .card {
    position: absolute;
    width: 560px; height: 320px;
    background: linear-gradient(160deg, var(--card-white) 40%, var(--card-grey));
    overflow: hidden;
    box-shadow: 0 12px 30px rgba(0,0,0,.45);
  }

  /* back card */
  .card-back { left: 70px; top: 110px; }
  .card-back .purple-field { position: absolute; inset: 0; }
  .card-back .brand { position: absolute; left: 40px; top: 128px; }
  .contact {
    position: absolute; left: 320px; top: 48px;
    color: var(--on-purple);
  }
  .contact-name { font-size: 25px; font-weight: 700; letter-spacing: .2px; }
  .contact-title { font-size: 16px; margin-top: 4px; }
  .contact-list { list-style: none; margin-top: 34px; }
  .contact-list li {
    display: flex; align-items: center; gap: 12px;
    font-size: 14px; margin-bottom: 14px;
  }
  .contact-list svg { width: 16px; height: 16px; flex: none; }

  /* brand lockup: plain name with one circle */
  .brand { display: flex; align-items: center; gap: 12px; }
  .brand-dot {
    flex: none; border-radius: 50%;
    background: var(--brand-purple);
  }
  .brand-name {
    font-weight: 400; color: var(--ink-dark); line-height: 1;
  }
  .card-back .brand-dot { width: 34px; height: 34px; }
  .card-back .brand-name { font-size: 30px; }

  /* front card */
  .card-front { left: 570px; top: 470px; }
  .card-front .brand { position: absolute; left: 95px; top: 112px; }
  .card-front .brand-dot { width: 48px; height: 48px; }
  .card-front .brand-name { font-size: 44px; }
  .band {
    position: absolute; left: 0; right: 0; bottom: 0; height: 40px;
    background: var(--brand-purple);
    border-top: 4px solid var(--brand-purple-light);
  }
</style>
</head>
<body>
<main class="stage">

  <section class="card card-back" aria-label="Business card back">
    <svg class="purple-field" viewBox="0 0 560 320" preserveAspectRatio="none" aria-hidden="true">
      <path d="M250 0 H560 V320 H290 C330 230 330 80 250 0 Z" fill="var(--brand-purple)"/>
    </svg>
    <div class="brand">
      <span class="brand-dot"></span>
      <div class="brand-name">CareerPathlane</div>
    </div>
    <div class="contact">
      <div class="contact-name">Daniel R Castillo</div>
      <div class="contact-title">Managing Director</div>
      <ul class="contact-list">
        <li>
          <svg viewBox="0 0 16 16" aria-hidden="true"><path d="M4 1 L6 5 L4.5 6.5 C5.5 8.5 7.5 10.5 9.5 11.5 L11 10 L15 12 L13.5 15 C7 15 1 9 1 2.5 Z" fill="currentColor"/></svg>
          555-014-2290
        </li>
        <li>
          <svg viewBox="0 0 16 16" aria-hidden="true"><rect x="1" y="3" width="14" height="10" rx="1" fill="currentColor"/><path d="M1.5 3.5 L8 9 L14.5 3.5" stroke="var(--brand-purple)" stroke-width="1.4" fill="none"/></svg>
          daniel@careerpathlane-demo.com
        </li>
        <li>
          <svg viewBox="0 0 16 16" aria-hidden="true"><g fill="none" stroke="currentColor" stroke-width="1.3"><circle cx="8" cy="8" r="6.5"/><ellipse cx="8" cy="8" rx="2.8" ry="6.5"/><path d="M1.5 8 H14.5 M2.5 4.8 H13.5 M2.5 11.2 H13.5"/></g></svg>
          www.careerpathlane-demo.com
        </li>
      </ul>
    </div>
  </section>

  <section class="card card-front" aria-label="Business card front">
    <div class="brand">
      <span class="brand-dot"></span>
      <div class="brand-name">CareerPathlane</div>
    </div>
    <div class="band"></div>
  </section>

</main>
</body>
</html>
```